Bright Harbor; Teaching Series Art.

Our church is going to be teaching a series of messages under the topic/title: Bright Harbor. Just looking for a simple design to help with this. I have uploaded a design that is an example of what we were thinking.

The point of the design is to communicate a new way of doing things (given some of the impact of the coronavirus) - although the background doesn't need to be too busy - just something simple, clean and modern.

Even though it's for a church, we don't need any religious art in the background (crosses, people praying, etc.) Looking for a similar feel background to the one we uploaded.

The only text should be Bright Harbor and maybe highlighting the word Bright somehow.

Font styles to use
Sans Serif

Requirements
Must have
• Title of "Bright Harbor" - no other text.

```html
<!DOCTYPE html>
<html lang="en">
<head>
<meta charset="utf-8">
<title>Bright Harbor – Series Art</title>
<link rel="stylesheet" href="https://fonts.googleapis.com/css2?family=Montserrat:ital,wght@0,400;0,700;1,700&display=swap">
<style>
  :root {
    --deep-navy: #0c1a3a;
    --teal-mist: #1d5a63;
    --indigo: #2a2d7a;
    --violet: #5a2d8c;
    --royal-blue: #2f5fd0;
    --sky-blue: #7fb8ff;
    --cyan-glow: #6ee6f0;
    --ink-blue: #1d3f9a;
    --white: #ffffff;
  }
  * { margin: 0; padding: 0; box-sizing: border-box; }
  html, body {
    width: 1200px; height: 2400px; overflow: hidden;
    background: var(--deep-navy);
  }
  .series-art { position: relative; width: 1200px; height: 2400px; }
  .panel {
    position: relative; width: 1200px; height: 800px; overflow: hidden;
    background:
      radial-gradient(ellipse 60% 70% at 20% 40%, rgba(40,120,120,.75), transparent 70%),
      radial-gradient(ellipse 55% 70% at 85% 30%, rgba(90,50,150,.7), transparent 70%),
      linear-gradient(135deg, var(--teal-mist) 0%, var(--indigo) 55%, var(--violet) 100%);
  }
  .panel svg { position: absolute; inset: 0; }
  .title {
    position: absolute; left: 0; width: 100%;
    font-family: "Montserrat", sans-serif; text-align: center; line-height: 1;
    white-space: nowrap; letter-spacing: -0.5px;
  }
  .title .highlight { font-style: italic; font-weight: 700; }
  .title .main { font-weight: 400; }

  .panel--glow .title {
    top: 358px; font-size: 72px; color: var(--sky-blue);
    text-shadow: 0 0 6px rgba(255,255,255,.6), 0 0 22px rgba(110,160,255,.6);
  }
  .panel--glow .title .highlight { color: var(--white); text-shadow: 0 0 10px var(--royal-blue), 0 0 24px var(--royal-blue); }

  .panel--diamond .title {
    top: 372px; left: 50px; font-size: 64px; color: var(--ink-blue);
  }
  .panel--diamond .title span { display: block; }
  .panel--diamond .title .main { font-weight: 700; margin-top: 6px; font-size: 62px; }

  .panel--squares .title {
    top: 430px; left: 20px; font-size: 68px; color: var(--white);
    text-shadow: 0 0 8px var(--royal-blue), 0 0 20px var(--royal-blue);
  }
  .panel--squares .title .highlight { color: var(--ink-blue); text-shadow: 0 0 4px #fff, 0 0 14px #fff; }
</style>
</head>
<body>
<main class="series-art">

  <section class="panel panel--glow">
    <svg width="1200" height="800" viewBox="0 0 1200 800" aria-hidden="true">
      <defs>
        <linearGradient id="blueTile" x1="0" y1="0" x2="1" y2="1">
          <stop offset="0" stop-color="#3a6ee0" stop-opacity=".75"/>
          <stop offset="1" stop-color="#1a2f8a" stop-opacity=".35"/>
        </linearGradient>
      </defs>
      <rect x="440" y="160" width="400" height="400" fill="url(#blueTile)" transform="rotate(40 640 360)"/>
      <g fill="#fff" opacity=".8">
        <circle cx="250" cy="470" r="3"/><circle cx="410" cy="610" r="4"/><circle cx="860" cy="520" r="3"/>
        <circle cx="980" cy="130" r="2"/><circle cx="170" cy="210" r="2"/><circle cx="1100" cy="650" r="3"/>
        <circle cx="720" cy="700" r="2"/><circle cx="520" cy="90" r="2"/>
      </g>
    </svg>
    <h1 class="title"><span class="highlight">Bright</span> <span class="main">Harbor</span></h1>
  </section>

  <section class="panel panel--diamond">
    <svg width="1200" height="800" viewBox="0 0 1200 800">
      <defs>
        <radialGradient id="splash" cx=".5" cy=".5" r=".5">
          <stop offset="0" stop-color="#2a50d8"/>
          <stop offset=".6" stop-color="#3f7fe8" stop-opacity=".85"/>
          <stop offset=".85" stop-color="#6ee6f0" stop-opacity=".45"/>
          <stop offset="1" stop-color="#6ee6f0" stop-opacity="0"/>
        </radialGradient>
      </defs>
      <ellipse role="img" aria-label="Blue paint splash texture" cx="650" cy="440" rx="420" ry="330" fill="url(#splash)"/>
      <rect x="485" y="275" width="330" height="330" fill="#fff" transform="rotate(45 650 440)"/>
      <g fill="#fff" opacity=".8">
        <circle cx="160" cy="250" r="3"/><circle cx="1050" cy="180" r="3"/><circle cx="690" cy="740" r="5"/>
        <circle cx="330" cy="90" r="2"/><circle cx="1120" cy="520" r="2"/>
      </g>
    </svg>
    <h1 class="title"><span class="highlight">Bright</span><span class="main">Harbor</span></h1>
  </section>

  <section class="panel panel--squares">
    <svg width="1200" height="800" viewBox="0 0 1200 800" aria-hidden="true">
      <defs>
        <linearGradient id="glassTile" x1="0" y1="0" x2="1" y2="1">
          <stop offset="0" stop-color="#c88cff" stop-opacity=".55"/>
          <stop offset="1" stop-color="#3a5ee8" stop-opacity=".45"/>
        </linearGradient>
        <filter id="edgeGlow" x="-20%" y="-20%" width="140%" height="140%">
          <feGaussianBlur stdDeviation="4"/>
        </filter>
      </defs>
      <g stroke="#f0c8ff" stroke-width="3" fill="url(#glassTile)">
        <rect x="120" y="330" width="260" height="260" transform="rotate(-15 250 460)"/>
        <rect x="300" y="230" width="300" height="300" transform="rotate(20 450 380)"/>
        <rect x="560" y="300" width="280" height="280" transform="rotate(-25 700 440)"/>
        <rect x="760" y="260" width="220" height="220" transform="rotate(15 870 370)"/>
        <rect x="860" y="420" width="200" height="200" transform="rotate(-10 960 520)"/>
        <rect x="420" y="500" width="240" height="240" transform="rotate(30 540 620)"/>
        <rect x="180" y="520" width="180" height="180" transform="rotate(10 270 610)"/>
      </g>
      <rect x="250" y="405" width="740" height="130" rx="6" fill="#fff" opacity=".45" filter="url(#edgeGlow)"/>
      <g fill="#fff" opacity=".8">
        <circle cx="1090" cy="80" r="3"/><circle cx="90" cy="130" r="2"/><circle cx="620" cy="60" r="2"/>
      </g>
    </svg>
    <h1 class="title"><span class="highlight">Bright</span> <span class="main">Harbor</span></h1>
  </section>

</main>
</body>
</html>
```